Income Tax Flyer - Updates Needed

Just need to update this flyer design and give it a new look. We would like to keep all the same wording but make it stand out a little more. Our selling point is the "Same Day Tax Advance up to $6,000"

Industry/Entity Type

Lending, Small Loans, Tax Services, Title Loans, Personal Loans

```html
<!DOCTYPE html>
<html lang="en">
<head>
<meta charset="utf-8">
<title>Same Day Tax Advance Flyer</title>
<link href="https://fonts.googleapis.com/css2?family=Montserrat:wght@600;700;800&family=Poppins:wght@500;600&display=swap" rel="stylesheet">
<style>
  :root {
    --green: #2b5533;
    --red: #ad232b;
    --white: #ffffff;
    --photo-light: #eef1f1;
    --photo-mid: #d9dede;
  }
  * { margin: 0; padding: 0; box-sizing: border-box; }
  html, body { width: 849px; height: 1200px; overflow: hidden; background: var(--white); }
  .flyer {
    position: relative;
    width: 849px;
    height: 1200px;
    overflow: hidden;
    background: var(--white);
    font-family: "Montserrat", sans-serif;
  }
  .hero-photo {
    position: absolute;
    left: 0; top: 0;
    width: 849px; height: 517px;
    background: radial-gradient(ellipse at 70% 45%, #c9d0d2 0%, var(--photo-mid) 30%, var(--photo-light) 65%, #f8f9f9 100%);
  }
  .hero-rule {
    position: absolute;
    left: 0; top: 117px;
    width: 514px; height: 2px;
    background: var(--green);
  }
  .brand {
    position: absolute;
    left: 528px; top: 70px;
    display: flex;
    align-items: center;
    gap: 10px;
    color: var(--green);
    font-family: "Montserrat", sans-serif;
    font-weight: 700;
  }
  .brand-mark {
    width: 30px; height: 30px;
    border-radius: 50%;
    background: var(--red);
  }
  .brand-name { font-size: 31px; line-height: 1; letter-spacing: -0.5px; }
  .brand-sub { font-size: 10px; letter-spacing: 3.6px; margin-top: 6px; }
  .headline {
    position: absolute;
    left: 46px; top: 192px;
    font-weight: 800;
    line-height: 1;
  }
  .headline-top { color: var(--red); font-size: 77px; letter-spacing: -1px; }
  .headline-mid { color: var(--green); font-size: 54px; margin-top: 10px; letter-spacing: -0.5px; }
  .headline-bottom { color: var(--green); margin-top: 8px; display: flex; align-items: baseline; gap: 18px; }
  .headline-bottom .lead { font-size: 50px; }
  .headline-bottom .amount { font-size: 77px; letter-spacing: -1px; }
  .hero-band {
    position: absolute;
    left: 0; top: 514px;
    width: 849px; height: 8px;
    background: var(--green);
  }
  .couple-photo {
    position: absolute;
    left: 446px; top: 322px;
    width: 386px; height: 386px;
    border-radius: 50%;
    border: 7px solid var(--green);
    background: radial-gradient(circle at 50% 40%, #e8dcd6 0%, #c9b6ac 35%, #51698f 70%, #3a4d6e 100%);
  }
  .pitch {
    position: absolute;
    left: 59px; top: 548px;
    color: var(--green);
    font-weight: 700;
    line-height: 1.3;
  }
  .pitch-line { font-size: 38px; }
  .pitch-accent { color: var(--red); font-size: 56px; font-weight: 800; line-height: 1.1; margin-top: 2px; }
  .benefits {
    position: absolute;
    left: 55px; top: 747px;
    width: 740px; height: 161px;
    border-radius: 22px;
    background: var(--red);
    display: flex;
  }
  .benefit {
    flex: 1;
    display: flex;
    flex-direction: column;
    align-items: center;
    padding-top: 14px;
    color: var(--white);
    font-family: "Poppins", sans-serif;
    font-weight: 500;
    font-size: 21px;
    line-height: 1.35;
    text-align: center;
  }
  .benefit-icon {
    width: 64px; height: 64px;
    border-radius: 50%;
    background: var(--white);
    border: 3px solid var(--green);
    display: flex; align-items: center; justify-content: center;
    margin-bottom: 12px;
  }
  .cta {
    position: absolute;
    left: 238px; top: 950px;
    width: 373px; height: 57px;
    display: flex;
    border: 1.5px solid var(--red);
    border-radius: 14px;
    overflow: hidden;
    font-family: "Poppins", sans-serif;
    font-weight: 600;
  }
  .cta-lead {
    width: 196px;
    display: flex; align-items: center; justify-content: center;
    color: var(--red);
    font-size: 29px;
    background: var(--white);
  }
  .cta-accent {
    flex: 1;
    display: flex; align-items: center; justify-content: center;
    color: var(--white);
    font-size: 37px;
    background: var(--red);
    padding-bottom: 4px;
  }
  .phone {
    position: absolute;
    left: 0; top: 1034px;
    width: 849px;
    text-align: center;
    color: var(--red);
    font-family: "Poppins", sans-serif;
    font-weight: 600;
    font-size: 28px;
  }
  .addresses {
    position: absolute;
    left: 18px; top: 1098px;
    width: 813px; height: 72px;
    display: flex;
  }
  .address {
    flex: 1;
    text-align: center;
    color: var(--green);
    font-family: "Poppins", sans-serif;
    font-weight: 600;
    font-size: 17px;
    padding-top: 6px;
  }
  .address + .address { border-left: 1.5px solid var(--red); }
  .footer-band {
    position: absolute;
    left: 0; top: 1187px;
    width: 849px; height: 13px;
    background: var(--green);
  }
</style>
</head>
<body>
<main class="flyer">
  <div class="hero-photo" role="img" aria-label="Softly blurred office scene with two people shaking hands"></div>
  <div class="hero-rule"></div>

  <div class="brand">
    <div class="brand-mark"></div>
    <div>
      <div class="brand-name">Ledger Lane</div>
      <div class="brand-sub">FINANCIAL GROUP</div>
    </div>
  </div>

  <h1 class="headline">
    <div class="headline-top">SAME DAY</div>
    <div class="headline-mid">TAX ADVANCE</div>
    <div class="headline-bottom"><span class="lead">UP TO</span><span class="amount">$6,000</span></div>
  </h1>

  <div class="hero-band"></div>
  <div class="couple-photo" role="img" aria-label="Smiling couple seated together at a table"></div>

  <div class="pitch">
    <div class="pitch-line">File your tax</div>
    <div class="pitch-line">and apply for an</div>
    <div class="pitch-accent">Easy Advance!</div>
  </div>

  <section class="benefits">
    <div class="benefit">
      <div class="benefit-icon">
        <svg width="36" height="36" viewBox="0 0 36 36" fill="none" stroke="#2b5533" stroke-width="2" stroke-linecap="round">
          <circle cx="18" cy="20" r="12"/>
          <path d="M15 4h6M18 4v4M28 9l2-2M8 9L6 7"/>
          <path d="M21 16.5c-1-1-4.5-1.2-4.5 1 0 2.3 4.8 1.2 4.8 3.6 0 2.2-3.6 2-5 .9M18.5 14v2M18.5 23.5v2"/>
        </svg>
      </div>
      <span>Available in<br>24 Hours or Less</span>
    </div>
    <div class="benefit">
      <div class="benefit-icon">
        <svg width="36" height="36" viewBox="0 0 36 36" fill="none" stroke="#2b5533" stroke-width="2" stroke-linecap="round" stroke-linejoin="round">
          <path d="M27 14a11 11 0 1 0-12 10"/>
          <path d="M18 11c-.8-.8-3.5-.8-3.5 .8s3.8 1 3.8 2.8-2.8 1.6-3.9.7M16.3 9v1.5M16.3 16.5V18"/>
          <path d="M20 31v-4l-3-3c-.8-.8.2-2 1-1.4l2 1.6V16c0-1.2 2-1.2 2 0v5l5 1c1.4.3 2 1.3 1.8 2.6L28 31"/>
        </svg>
      </div>
      <span>Choose Your<br>Loan Amount</span>
    </div>
    <div class="benefit">
      <div class="benefit-icon">
        <svg width="36" height="36" viewBox="0 0 36 36" fill="none" stroke="#2b5533" stroke-width="2" stroke-linecap="round" stroke-linejoin="round">
          <rect x="14" y="4" width="14" height="22" rx="1"/>
          <circle cx="21" cy="15" r="3"/>
          <path d="M5 24l6-6c1.5-1.5 3.5-1 5 0l3 2c1 .7.3 2.3-1 1.8L15 21M7 30l3-3h7l4-4"/>
        </svg>
      </div>
      <span>Quick and Easy</span>
    </div>
  </section>

  <div class="cta">
    <span class="cta-lead">Contact Us</span>
    <span class="cta-accent">Today!</span>
  </div>

  <div class="phone">Phone Number</div>

  <div class="addresses">
    <div class="address">Address line 1</div>
    <div class="address">Address line 2</div>
    <div class="address">Address line 3</div>
  </div>

  <div class="footer-band"></div>
</main>
</body>
</html>
```